Convert paper form into fillable PDF form.

Hello,

Task is pretty simple just time consuming. Basically I run a nutrition business and i want to convert my paper based client intake forms into digital PDF forms that can be filled out on your computer. This way I can email clients the forms and they can fill them out and email them back, saving paper and time.

All the content has been written, i just need YOU the designer to convert it to a USER FRIENDLY PDF form!

Any questions please let me know!

Nutrition

```html
<!DOCTYPE html>
<html lang="en">
<head>
<meta charset="utf-8">
<title>Verdelo Client Intake Form</title>
<link rel="stylesheet" href="https://fonts.googleapis.com/css2?family=Questrial&family=Didact+Gothic&family=Tinos&family=Arimo&display=swap">
<style>
  :root {
    --backdrop: #e6e6e6;
    --sheet: #ffffff;
    --ink: #111111;
    --body-ink: #333333;
    --field-fill: #dde3fb;
    --field-line: #3a3a3a;
    --link: #1a2fd0;
    --brand: #2f3474;
    --brand-dot: #8cae3c;
  }
  * { margin: 0; padding: 0; box-sizing: border-box; }
  html, body { width: 1200px; height: 1000px; overflow: hidden; background: var(--backdrop); }
  .sheet {
    position: absolute; left: 40px; width: 1120px; background: var(--sheet);
    box-shadow: 0 1px 4px rgba(0,0,0,.18); overflow: hidden;
  }
  .sheet--intro { top: 30px; height: 560px; }
  .sheet--habits { top: 620px; height: 350px; }
  .contact {
    position: absolute; right: 78px; text-align: right;
    font-family: "Tinos", "Times New Roman", serif; font-size: 19px; line-height: 22px; color: var(--ink);
  }
  .contact a { color: var(--link); text-decoration: underline; }
  .sheet--intro .contact { top: 22px; }
  .sheet--habits .contact { top: 22px; }
  .brand {
    position: absolute; left: 50px; top: 30px; display: flex; align-items: center; gap: 22px;
  }
  .brand-dot { width: 90px; height: 90px; border-radius: 50%; background: var(--brand-dot); }
  .brand-name {
    font-family: "Questrial", sans-serif; font-size: 60px; letter-spacing: 8px; color: var(--brand);
  }
  .form-title {
    position: absolute; top: 150px; left: 0; width: 100%; text-align: center;
    font-family: "Didact Gothic", sans-serif; font-weight: 700; font-size: 31px; color: var(--ink);
    -webkit-text-stroke: 0.6px var(--ink);
  }
  .form-note {
    position: absolute; top: 208px; left: 120px; width: 900px; text-align: center;
    font-family: "Didact Gothic", sans-serif; font-style: italic; font-size: 19px; line-height: 27px; color: var(--body-ink);
  }
  .label {
    position: absolute; font-family: "Didact Gothic", sans-serif; font-size: 19px; color: var(--body-ink);
  }
  .field {
    position: absolute; background: var(--field-fill); border-bottom: 1px solid var(--field-line);
    font-family: "Arimo", Arial, sans-serif; color: var(--ink); padding-left: 6px;
  }
  .field--name-value { font-size: 28px; line-height: 44px; }
  .field--mark { font-size: 22px; line-height: 40px; padding-left: 4px; }
  .section-heading {
    position: absolute; left: 100px; top: 120px;
    font-family: "Didact Gothic", sans-serif; font-size: 22px; color: var(--ink);
    -webkit-text-stroke: 0.5px var(--ink);
  }
</style>
</head>
<body>
  <section class="sheet sheet--intro">
    <div class="brand">
      <span class="brand-dot"></span>
      <span class="brand-name">VERDELO</span>
    </div>
    <div class="contact">
      <div>0400 555 210</div>
      <div><a href="mailto:hello@verdelo.com.au">hello@verdelo.com.au</a></div>
      <div>www.verdelo.com.au</div>
    </div>
    <h1 class="form-title">Client Intake Form</h1>
    <p class="form-note">Please fill out the following questions as best you can.&nbsp; If there is a particular question you don’t understand or want to fill out, we can discuss them at our first meeting. Thank you.</p>

    <span class="label" style="left:99px; top:292px;">Name</span>
    <div class="field field--name-value" style="left:155px; top:267px; width:393px; height:45px;">Sample Client</div>
    <span class="label" style="left:723px; top:292px;">Date</span>
    <div class="field" style="left:769px; top:267px; width:234px; height:45px;"></div>

    <span class="label" style="left:99px; top:338px;">Phone (h)</span>
    <div class="field" style="left:188px; top:313px; width:243px; height:45px;"></div>
    <span class="label" style="left:432px; top:338px;">(w)</span>
    <div class="field" style="left:460px; top:313px; width:262px; height:45px;"></div>
    <span class="label" style="left:729px; top:338px;">(m)</span>
    <div class="field" style="left:764px; top:313px; width:243px; height:45px;"></div>

    <div class="field" style="left:171px; top:359px; width:831px; height:45px;"></div>
  </section>

  <section class="sheet sheet--habits">
    <div class="contact">
      <div>0400 555 210</div>
      <div><a href="mailto:hello@verdelo.com.au">hello@verdelo.com.au</a></div>
      <div>www.verdelo.com.au</div>
    </div>
    <h2 class="section-heading">Nutrition and Dietary Habits</h2>
    <span class="label" style="left:100px; top:176px;">How many meals do you typically eat per day?</span>
    <div class="field field--mark" style="left:533px; top:154px; width:94px; height:41px;">x</div>
    <span class="label" style="left:633px; top:176px;">Do you snack?</span>
    <div class="field field--mark" style="left:771px; top:154px; width:94px; height:41px;">x</div>
  </section>
</body>
</html>
```